We specialize in pizza, pasta and salads and are now offering TAKE & BAKE and GRAB & GO ...

Looking for either a 8.5" x 11" or similar for a instore display. WILL BE ON A SWIVELING HOLDER to catch customers attention.

**THIS IS A DOUBLE SIDED PRINT**

ONE SIDE will consist of WHAT'S FOR DINNER TONIGHT? and the following:
* Take & Bake"
* "Baked Pasta"
* Freshly made in house
* Lasagna
$13.50
- please include attached closeup picture and logo

THE OTHER SIDE will consist of
mini charcutier board.
* snack size charcutier delight *
* Enjoy the flavors of gourmet snacking, all in one convenient box!

PRICE $8.99

Winning design will be commissioned to design labels for "grab and go" for take and bake pasta, charcuterie box, pasta salads, candy etc.

Thank you and please do not hesitate to ask any questions.

www.calderipizza.ca
www.fernloop.ca
Logo to be interchanged as they are affiliated meaning FernLoop is a brand within Calderi pizza.

Target Market(s)

our target market is customers who have already entered our business. This is to upsel

Industry/Entity Type

We are in a self serve enviroment and target business people

Requirements
Must have
• must be clean and catchy. We are located in a professional business community.
Nice to have
• Must be appealing, appetizing and utilize our website colors
Should not have
• should not have any carton drawings and not be cluttered (busy)

```html
<!DOCTYPE html>
<html lang="en">
<head>
<meta charset="utf-8">
<title>FernLoop Catering – What's for Dinner Tonight?</title>
<link rel="stylesheet" href="https://fonts.googleapis.com/css2?family=Barlow+Condensed:wght@300;400;500;700&family=Montserrat:wght@600&display=swap">
<style>
  :root {
    --backdrop: #c4c4c4;
    --paper: #ffffff;
    --navy: #141c3f;
    --orange: #f15a29;
    --food-light: #ecd3a0;
    --food-mid: #c98a3a;
    --food-dark: #6e4318;
  }
  * { margin: 0; padding: 0; box-sizing: border-box; }
  html, body {
    width: 1199px; height: 1200px; overflow: hidden;
    background: var(--backdrop);
  }
  .flyer {
    position: absolute; left: 197px; top: 80px;
    width: 804px; height: 1039px;
    background: var(--paper);
    overflow: hidden;
    font-family: "Barlow Condensed", "Arial Narrow", sans-serif;
    color: var(--navy);
  }
  .photo-layer { position: absolute; inset: 0; }
  .brand {
    position: absolute; left: 67px; top: 56px;
    width: 210px; text-align: center;
  }
  .brand-dot {
    display: block; margin: 0 auto 18px;
    width: 82px; height: 82px; border-radius: 50%;
    border: 4px solid var(--navy);
  }
  .brand-name {
    font-family: "Montserrat", sans-serif; font-weight: 600;
    font-size: 30px; color: var(--navy); letter-spacing: 0.2px;
  }
  .headline {
    position: absolute; left: 64px; top: 250px;
    text-transform: uppercase; line-height: 0.98;
  }
  .headline .lead { font-weight: 300; font-size: 76px; letter-spacing: 0.5px; display: block; }
  .headline .strong { font-weight: 700; font-size: 94px; display: block; }
  .offer-card {
    position: absolute; left: 37px; top: 535px;
    width: 380px; height: 282px;
    background: var(--orange); border-radius: 26px;
  }
  .offer-list {
    position: absolute; left: 67px; top: 566px;
    list-style: none; color: #fff;
    font-size: 29px; font-weight: 400; line-height: 35px;
  }
  .photo-curve { position: absolute; inset: 0; pointer-events: none; }
  .dinner-price {
    position: absolute; left: 169px; top: 732px;
    width: 170px; height: 65px; border-radius: 9px;
    background: var(--navy); color: #fff;
    font-size: 36px; font-weight: 500;
    display: flex; align-items: center; justify-content: center;
  }
  .snack-info {
    position: absolute; left: 67px; top: 843px;
    font-size: 18px; line-height: 24px; color: var(--navy);
  }
  .snack-price {
    position: absolute; left: 0; top: 935px;
    width: 277px; height: 65px; border-radius: 0 9px 9px 0;
    background: var(--orange); color: #fff;
    font-size: 37px; font-weight: 500;
    padding-left: 67px; display: flex; align-items: center;
  }
  .partner-name {
    position: absolute; right: 54px; top: 962px;
    font-size: 40px; font-weight: 400; letter-spacing: 1px;
    color: var(--navy); text-transform: uppercase;
  }
</style>
</head>
<body>
  <main class="flyer">
    <svg class="photo-layer" width="804" height="1039" viewBox="0 0 804 1039">
      <defs>
        <radialGradient id="pasta-tones" cx="0.55" cy="0.45" r="0.75">
          <stop offset="0" stop-color="var(--food-light)"/>
          <stop offset="0.45" stop-color="var(--food-mid)"/>
          <stop offset="1" stop-color="var(--food-dark)"/>
        </radialGradient>
      </defs>
      <path role="img" aria-label="Close-up photo of baked pasta with stretching melted cheese lifted from a dish"
            fill="url(#pasta-tones)"
            d="M177,0 H804 V851 C700,890 560,900 470,862 C430,760 400,600 415,457 C420,300 330,100 177,0 Z"/>
    </svg>

    <div class="brand">
      <span class="brand-dot"></span>
      <div class="brand-name">FernLoop</div>
    </div>

    <h1 class="headline">
      <span class="lead">What's for</span>
      <span class="strong">Dinner</span>
      <span class="strong">Tonight?</span>
    </h1>

    <div class="offer-card"></div>
    <ul class="offer-list">
      <li>* Take &amp; Bake"</li>
      <li>* "Baked Pasta"</li>
      <li>* Freshly made in house</li>
      <li>* Lasagna</li>
    </ul>

    <svg class="photo-curve" width="804" height="1039" viewBox="0 0 804 1039">
      <path role="img" aria-label="Close-up photo of baked pasta with stretching melted cheese lifted from a dish"
            fill="url(#pasta-tones)"
            d="M400,535 H420 V817 H400 C405,760 404,620 400,535 Z" opacity="0"/>
      <path d="M430,250 C470,330 480,430 460,560 C450,640 440,700 425,760"
            fill="none" stroke="#ffffff" stroke-width="4" stroke-linecap="round"/>
    </svg>

    <div class="dinner-price">$13.50</div>

    <div class="snack-info">
      <p>mini charcurterie board.</p>
      <p>* snack size charcutier delight *</p>
      <p>* Enjoy the flavors of gourment snacking, all in one convenient box!</p>
    </div>

    <div class="snack-price">PRICE $8.99</div>

    <div class="partner-name">Calderi Pizza</div>
  </main>
</body>
</html>
```